Unique Flyer Project - www.plumorchardpanel.com.au

The purpose of this flyer is trying to get recipients to visit the website www.plumorchardpanel.com.au and sign up to the offer. I need it to be simple/to the point, eye catching and professional. I will post up a basic idea I have but feel free to put your own spin on it if you think you have great ideas to get people to visit the site, if not then just improve upon the quality of mine and make it look like a respected company.

I also think a red band or something that REALLY catches the eye highlighting one of the important aspects of the flyer (the domain?) could be great so even if someone is about to put it in the bin, the popping red-on-white-background catches their eye so they end up looking at and reading the flyer.

I would also love a VERY SIMPLE design for the backside of the flyer, just a red box/band (whatever you think is good) with the domain 'www.plumorchardpanel.com.au' in it. NOTHING ELSE! Just so if it's floating around the table and it's upside down, there's something eye catching that might entice the householder to look at it.

DESIGN IS FOR DL FLYER: 99mm X 210mm

Target Market(s)

Australian Residents interested in earning money from home.

Industry/Entity Type

It Company

Requirements
Must have
• Eye catching (mainly red band/box/bar on front & back page), SIMPLE, elegant/professional.
Should not have
• ANYTHING unnecessary to the reader that will distract them from the ultimate point - GET PAID TO DO SURVEYS FROM YOUR OWN HOME ON THE COMPUTER!

```html
<!DOCTYPE html>
<html lang="en">
<head>
<meta charset="utf-8">
<title>Plum Orchard Panel – DL Flyer</title>
<link href="https://fonts.googleapis.com/css2?family=Anton&family=Source+Sans+3:wght@700&family=Montserrat:wght@500&family=Open+Sans:wght@800&display=swap" rel="stylesheet">
<style>
  :root {
    --flyer-red: #ec1c24;
    --ink: #231f20;
    --band-black: #050505;
    --paper: #ffffff;
    --flag-blue: #1f2a78;
  }
  html, body {
    margin: 0;
    padding: 0;
    width: 1200px;
    height: 1143px;
    overflow: hidden;
    background: var(--paper);
  }
  .flyer {
    position: relative;
    width: 1200px;
    height: 1143px;
    background: var(--paper);
  }
  .front-side {
    position: absolute;
    left: 0; top: 0;
    width: 1200px; height: 566px;
    background: var(--flyer-red);
  }
  .front-panel {
    position: absolute;
    left: 15px; top: 15px;
    width: 1170px; height: 536px;
    background: var(--paper);
    overflow: hidden;
  }
  .mouse-art {
    position: absolute;
    left: 25px; top: 48px;
    width: 257px; height: 80px;
    border-radius: 50% 50% 40% 40%;
    background: radial-gradient(ellipse at 45% 70%, #e0321f 0%, #8a8a8a 55%, #3a3a3a 100%);
  }
  .headline {
    position: absolute;
    left: 288px; top: 26px;
    margin: 0;
    width: 840px; height: 80px;
  }
  .headline svg { display: block; }
  .headline__text {
    font-family: "Source Sans 3", "Myriad Pro", sans-serif;
    font-weight: 700;
    font-size: 96px;
    fill: var(--band-black);
  }
  .pitch {
    position: absolute;
    left: 31px;
    margin: 0;
    font-family: "Source Sans 3", "Myriad Pro", sans-serif;
    font-weight: 700;
    line-height: 1;
    white-space: nowrap;
  }
  .pitch--question { top: 152px; font-size: 60px; letter-spacing: 3.6px; color: var(--flyer-red); }
  .pitch--earn { top: 217px; font-size: 53px; letter-spacing: 2.6px; color: var(--ink); }
  .pitch--earn .amount { color: var(--flyer-red); }
  .pitch--hours { top: 282px; font-size: 31px; letter-spacing: 2.2px; color: var(--ink); }
  .cash-art {
    position: absolute;
    left: 951px; top: 208px;
    width: 200px; height: 110px;
    transform: rotate(-8deg);
    border-radius: 6px;
    background: linear-gradient(135deg, #e3c84a 0%, #d6a12a 50%, #8fa54a 100%);
  }
  .domain-band {
    position: absolute;
    left: 0; top: 326px;
    width: 1170px; height: 105px;
    background: var(--band-black);
  }
  .domain-band svg { display: block; }
  .domain-band__text {
    font-family: "Anton", "Oswald", sans-serif;
    font-size: 84px;
    fill: var(--flyer-red);
    stroke: var(--paper);
    stroke-width: 1.5px;
    paint-order: stroke;
  }
  .flag {
    position: absolute;
    top: 468px;
    width: 108px; height: 54px;
    background: var(--flag-blue);
  }
  .flag--left { left: 31px; }
  .flag--right { left: 1027px; }
  .availability {
    position: absolute;
    left: 188px; top: 477px;
    width: 794px;
    margin: 0;
    text-align: center;
    font-family: "Montserrat", "Optima", sans-serif;
    font-weight: 500;
    font-size: 28px;
    letter-spacing: 1.5px;
    line-height: 1.2;
    color: var(--ink);
    white-space: nowrap;
  }
  .back-side {
    position: absolute;
    left: 0; top: 585px;
    width: 1200px; height: 558px;
    background: var(--flyer-red);
  }
  .back-side svg {
    position: absolute;
    left: 0; top: 250px;
  }
  .back-side__domain {
    font-family: "Open Sans", "Arial Black", sans-serif;
    font-weight: 800;
    font-size: 48px;
    fill: var(--paper);
  }
</style>
</head>
<body>
<main class="flyer">
  <section class="front-side">
    <div class="front-panel">
      <div class="mouse-art" role="img" aria-label="Computer mouse with red glow and cable"></div>
      <h1 class="headline">
        <svg width="840" height="80" viewBox="0 0 840 80">
          <text class="headline__text" x="0" y="74" textLength="840" lengthAdjust="spacingAndGlyphs">PLUM ORCHARD PANEL</text>
        </svg>
      </h1>
      <p class="pitch pitch--question">COULD YOU USE AN EXTRA INCOME?</p>
      <p class="pitch pitch--earn">EARN AS MUCH AS <span class="amount">$50</span> PER SURVEY!</p>
      <p class="pitch pitch--hours">WORK FROM HOME AND CHOOSE YOUR OWN HOURS!</p>
      <div class="cash-art" role="img" aria-label="Fanned Australian fifty dollar notes"></div>
      <div class="domain-band">
        <svg width="1170" height="105" viewBox="0 0 1170 105">
          <text class="domain-band__text" x="31" y="88" textLength="1097" lengthAdjust="spacingAndGlyphs">WWW.PLUMORCHARDPANEL.COM.AU</text>
        </svg>
      </div>
      <div class="flag flag--left" role="img" aria-label="Australian flag"></div>
      <p class="availability">NOW OPEN TO RESIDENTS OF AUSTRALIA</p>
      <div class="flag flag--right" role="img" aria-label="Australian flag"></div>
    </div>
  </section>
  <section class="back-side">
    <svg width="1200" height="70" viewBox="0 0 1200 70">
      <text class="back-side__domain" x="166" y="56" textLength="874" lengthAdjust="spacingAndGlyphs">WWW.PLUMORCHARDPANEL.COM.AU</text>
    </svg>
  </section>
</main>
</body>
</html>
```